ZEPRILO.COM is a premium domain sales company. Our competitors are companies like vastplots.example, getparcels.example, peerwords.example. Our current site is at www.zeprilos.example.

We want to have the ability to search for domains, to highlight special offers and have some testimonials on the index page.

The logo for the site is attached.

Please be sure that the order form fits on the screen without scrolling the page. I want the entire form, including the submit button to fit without any page scrolling.

Delivered product - INDEX PAGE, ORDER FORM AND CONTENT PAGE PSDs.

Target Market(s)

Small to Medium business professionals

Industry/Entity Type

It Company

Requirements
Must have
• 1. List of domains for sale
2. Simple search box with button to run the search
3. link for advanced search
4. testimonial area. Note - this can be a small box where a different testimonial is displayed on each page load.
Nice to have
• Would like the site to have some white space. Don't want a heavily packed website. Give it an "airy" feel.

```html
<!DOCTYPE html>
<html lang="en">
<head>
<meta charset="utf-8">
<title>ZEPRILO.COM – Premium Domains</title>
<link href="https://fonts.googleapis.com/css2?family=Montserrat:wght@400;600;700&family=Raleway:ital,wght@0,400;0,500;0,600;0,700;0,800;1,500&family=Noto+Serif:wght@400&display=swap" rel="stylesheet">
<style>
:root{
  --brand-blue:#0a4f9e;
  --nav-blue:#0d5aa7;
  --link-blue:#1b5fae;
  --button-blue:#6fa8dc;
  --green:#3d9a1c;
  --green-dark:#2a7a10;
  --orange:#f7a800;
  --text:#333;
  --muted:#777;
  --row-a:#eeeeee;
  --row-b:#f7f7f7;
  --band:#efefef;
  --footer:#86b4dc;
  --white:#fff;
}
*{box-sizing:border-box;margin:0;padding:0}
html,body{width:916px;height:1200px;overflow:hidden}
body{position:relative;background:var(--white);font-family:"Raleway",sans-serif;color:var(--text);font-variant-numeric:lining-nums}
.abs{position:absolute}
a{color:inherit;text-decoration:none}

/* header */
.logo{left:108px;top:29px;display:flex;align-items:center;gap:5px;font-family:"Raleway",sans-serif;font-weight:800;font-size:16px;color:var(--brand-blue);letter-spacing:-.2px;white-space:nowrap}
.logo .dot{width:10px;height:10px;border-radius:50%;background:var(--green)}
.topbar{right:108px;top:8px;display:flex;gap:12px;font-family:"Montserrat",sans-serif;font-size:9px;color:#222}
.topbar .phone b{font-weight:600}
.topbar .phone span{color:#555}
.topbar .sep{width:6px}
.mainnav{left:240px;top:27px;width:568px;height:22px;background:var(--nav-blue);display:flex;justify-content:flex-end;align-items:center;gap:24px;padding-right:10px;font-family:"Montserrat",sans-serif;font-size:11px;color:var(--white);letter-spacing:.3px}
.navrule{left:240px;top:52px;width:568px;height:3px;background:#dfe3e8}
.cart{right:112px;top:60px;font-family:"Montserrat",sans-serif;font-size:10px;color:var(--link-blue);display:flex;align-items:center;gap:4px}

/* hero */
.hero{left:0;top:80px;width:916px;height:266px;background:linear-gradient(180deg,#cfe3f3 0%,#e6f0f8 45%,#c7d6a4 72%,#8aa442 100%)}
.searchcard{left:118px;top:97px;width:329px;height:158px;background:rgba(236,243,250,.92);border-radius:3px;box-shadow:0 0 6px rgba(0,0,0,.08)}
.searchcard h1{position:absolute;left:10px;top:6px;font-family:"Noto Serif",serif;font-weight:400;font-size:32px;color:var(--brand-blue);letter-spacing:-.6px;white-space:nowrap}
.searchcard .sub{position:absolute;left:11px;top:43px;font-size:12.5px;color:#222}
.searchbar{position:absolute;left:11px;top:66px;width:307px;height:36px;background:#e3e8ed;border:1px solid #cfd6dc;border-radius:3px}
.searchbar .field{position:absolute;left:6px;top:5px;width:200px;height:24px;background:#d4dde6;font-size:12px;color:#555;padding:5px 0 0 10px}
.searchbar .ext{position:absolute;left:207px;top:5px;width:50px;height:24px;background:#f3f3f3;border:1px solid #ccc;font-size:12px;color:#555;padding:4px 0 0 6px}
.searchbar .go{position:absolute;left:261px;top:3px;width:43px;height:27px;background:linear-gradient(#ffc21a,var(--orange));border:1px solid #d48d00;border-radius:3px;font-weight:700;font-size:11px;color:#333;text-align:center;line-height:25px}
.searchcard .hint{position:absolute;left:11px;top:116px;font-size:9px;color:#222}
.searchcard .adv{position:absolute;left:8px;top:136px;font-family:"Montserrat",sans-serif;font-weight:600;font-size:10px;color:var(--brand-blue)}

/* featured */
.sec-title{font-family:"Montserrat",sans-serif;font-weight:700;font-size:18px;color:var(--brand-blue)}
.featured-title{left:107px;top:361px}
.seemore{left:548px;top:364px;background:var(--green-dark);color:var(--white);font-family:"Montserrat",sans-serif;font-size:8px;padding:3px 5px;border-radius:2px}
.domains{left:107px;top:391px;width:485px;border-collapse:collapse;font-size:10px}
.domains th{height:30px;background:linear-gradient(#1a64b4,#0b4b93);color:var(--white);font-family:"Montserrat",sans-serif;font-weight:400;font-size:12px;text-align:left;padding-left:14px}
.domains th:first-child{border-radius:3px 0 0 0}
.domains th:last-child{border-radius:0 3px 0 0}
.domains td{height:28.6px;padding-left:14px;color:#555}
.domains td.opt{padding-left:4px}
.domains tr:nth-child(odd) td{background:var(--row-a)}
.domains tr:nth-child(even) td{background:var(--row-b)}
.buy{display:inline-flex;align-items:center;gap:5px;background:var(--button-blue);color:var(--white);font-size:10px;padding:3px 5px;border-radius:2px}

/* advanced */
.advanced{left:613px;top:364px;width:195px;height:256px;background:linear-gradient(#f2f2f2,#fafafa);border:1px solid #ddd;border-bottom:3px solid #ccc;border-radius:3px}
.advanced h2{position:absolute;left:14px;top:12px;font-family:"Montserrat",sans-serif;font-weight:600;font-size:13px;color:#333}
.advanced label{position:absolute;font-size:9px;font-weight:700;color:#222}
.input{position:absolute;background:var(--white);border:1px solid #ccc;border-radius:2px}
.checks{position:absolute;left:16px;top:116px;display:flex;gap:6px;font-size:9px;color:#222}
.checks span{display:flex;align-items:center;gap:3px}
.box{width:10px;height:10px;border:1px solid #6b8fbe;background:#e8f0fa;display:inline-flex}
.to{position:absolute;font-size:9px;color:#222}
.find{position:absolute;left:16px;top:210px;width:161px;height:28px;background:linear-gradient(#4dab22,#267a0c);border:1px solid #1f6609;border-radius:3px;color:var(--white);font-family:"Montserrat",sans-serif;font-weight:700;font-size:12px;text-align:center;line-height:26px}

/* features band */
.band{left:0;top:655px;width:916px;height:225px;background:linear-gradient(#ececec,#f6f6f6)}
.col-title{font-family:"Raleway",sans-serif;font-weight:500;font-size:16px;color:var(--brand-blue)}
.feature{display:flex;gap:7px;align-items:flex-start}
.feature h3{font-weight:500;font-size:12px;color:var(--link-blue);margin-top:1px}
.feature p{font-size:9px;color:var(--muted);line-height:11px}
.promo{left:613px;top:674px;width:196px;height:174px;border:1px solid #ddd;border-radius:3px;overflow:hidden;background:linear-gradient(180deg,#6cbf1a 0%,#4f9d10 40%,#fdfdfd 41%,#e8e8e8 100%)}
.promo .get{position:absolute;left:7px;top:4px;color:var(--white);font-family:"Noto Serif",serif;line-height:1}
.promo .easy{position:absolute;left:13px;top:122px;font-family:"Noto Serif",serif;font-size:15px;color:#111;line-height:15px}

/* testimonials */
.testi-title{left:108px;top:900px;display:flex;align-items:center;gap:4px;font-family:"Raleway",sans-serif;font-weight:400;font-size:18px;color:#222}
.quotebox{left:146px;top:934px;width:663px;height:71px;border:1px solid #ddd;border-radius:3px;box-shadow:0 2px 3px rgba(0,0,0,.08);padding:14px 28px 0 14px;font-style:italic;font-weight:500;font-size:10.5px;line-height:13px;color:#444}
.quote-tail{left:656px;top:1003px}
.quote-by{left:668px;top:1018px;font-size:10px;font-weight:600;color:#222}

/* footer */
.footer{left:0;top:1063px;width:916px;height:137px;background:var(--footer);color:var(--white)}
.fcol{position:absolute;top:12px;font-size:9px;line-height:13px}
.fcol h4{font-family:"Montserrat",sans-serif;font-weight:600;font-size:10px;margin-bottom:4px}
.frule{position:absolute;left:102px;top:100px;width:702px;height:1px;background:rgba(255,255,255,.6)}
.copy{position:absolute;left:409px;top:112px;font-size:9px}
.social{position:absolute;left:104px;top:112px;display:flex;gap:8px}
.social i{width:12px;height:12px;border-radius:50%;background:var(--white);display:block}
</style>
</head>
<body>

<header>
  <a class="abs logo" href="#"><span class="dot"></span>ZEPRILO.COM</a>
  <div class="abs topbar">
    <span class="phone"><b>SALES:</b> <span>+00.5550.1234</span></span>
    <span class="phone"><b>SUPPORT:</b> <span>+00.5550.5678</span></span>
    <span class="sep"></span>
    <a href="#">LIVE CHAT</a><a href="#">CONTACT US</a><a href="#">PORTAL</a><a href="#">BLOG</a>
  </div>
  <nav class="abs mainnav">
    <a href="#">HOME</a><a href="#">DELETING DOMAINS</a><a href="#">DOMAINS FOR SALE</a><a href="#">TESTIMONIALS</a><a href="#">SUPPORT</a>
  </nav>
  <div class="abs navrule"></div>
  <a class="abs cart" href="#">
    <svg width="11" height="10" viewBox="0 0 11 10"><path d="M0 1h2l2 5h5l1.5-4H3" fill="none" stroke="#1b5fae" stroke-width="1.4"/><circle cx="4.5" cy="8.5" r="1" fill="#1b5fae"/><circle cx="8.5" cy="8.5" r="1" fill="#1b5fae"/></svg>Cart
  </a>
</header>

<section>
  <div class="abs hero" role="img" aria-label="Photo of a businessman working on a laptop while sitting in tall grass under a clear sky"></div>
  <div class="abs searchcard">
    <h1>Find Your Domain</h1>
    <p class="sub">You can find the best name for your business...</p>
    <div class="searchbar">
      <div class="field">Enter Domain Name</div>
      <div class="ext">.Com <svg width="7" height="5" viewBox="0 0 7 5"><path d="M0 0h7L3.5 4z" fill="#666"/></svg></div>
      <div class="go">Go!</div>
    </div>
    <p class="hint">Start your search by entering the first character of the domain name.</p>
    <a class="adv" href="#">Advanced Search ►</a>
  </div>
</section>

<section>
  <h2 class="abs sec-title featured-title">Featured Domains</h2>
  <a class="abs seemore" href="#">See More</a>
  <table class="abs domains">
    <thead><tr><th style="width:197px">Domain</th><th style="width:111px">Category</th><th style="width:81px">Price</th><th>Option</th></tr></thead>
    <tbody>
      <tr><td>CompanyName.com</td><td>Contracts</td><td>$9,400</td><td class="opt"><span class="buy">Buy Now <svg width="10" height="9" viewBox="0 0 10 9"><path d="M1 3h8v6H1zM3 3V1h4v2M3 5h1M6 5h1M3 7h1M6 7h1" fill="none" stroke="#fff"/></svg></span></td></tr>
      <tr><td>CompanyName.com</td><td>Careers</td><td>$5,990</td><td class="opt"><span class="buy">Buy Now <svg width="10" height="9" viewBox="0 0 10 9"><path d="M1 3h8v6H1zM3 3V1h4v2M3 5h1M6 5h1M3 7h1M6 7h1" fill="none" stroke="#fff"/></svg></span></td></tr>
      <tr><td>CompanyName.com</td><td>Maps</td><td>$7,995</td><td class="opt"><span class="buy">Buy Now <svg width="10" height="9" viewBox="0 0 10 9"><path d="M1 3h8v6H1zM3 3V1h4v2M3 5h1M6 5h1M3 7h1M6 7h1" fill="none" stroke="#fff"/></svg></span></td></tr>
      <tr><td>CompanyName.com</td><td>E-Commerce</td><td>$5,790</td><td class="opt"><span class="buy">Buy Now <svg width="10" height="9" viewBox="0 0 10 9"><path d="M1 3h8v6H1zM3 3V1h4v2M3 5h1M6 5h1M3 7h1M6 7h1" fill="none" stroke="#fff"/></svg></span></td></tr>
      <tr><td>CompanyName.com</td><td>Rock and Pop</td><td>$6,395</td><td class="opt"><span class="buy">Buy Now <svg width="10" height="9" viewBox="0 0 10 9"><path d="M1 3h8v6H1zM3 3V1h4v2M3 5h1M6 5h1M3 7h1M6 7h1" fill="none" stroke="#fff"/></svg></span></td></tr>
      <tr><td>CompanyName.com</td><td>Furniture</td><td>$5,495</td><td class="opt"><span class="buy">Buy Now <svg width="10" height="9" viewBox="0 0 10 9"><path d="M1 3h8v6H1zM3 3V1h4v2M3 5h1M6 5h1M3 7h1M6 7h1" fill="none" stroke="#fff"/></svg></span></td></tr>
      <tr><td>CompanyName.com</td><td>Candy</td><td>$5,390</td><td class="opt"><span class="buy">Buy Now <svg width="10" height="9" viewBox="0 0 10 9"><path d="M1 3h8v6H1zM3 3V1h4v2M3 5h1M6 5h1M3 7h1M6 7h1" fill="none" stroke="#fff"/></svg></span></td></tr>
    </tbody>
  </table>

  <form class="abs advanced">
    <h2>Advanced Search</h2>
    <label style="left:16px;top:43px">Keyword(s):</label>
    <div class="input" style="left:14px;top:60px;width:166px;height:23px"></div>
    <label style="left:16px;top:95px">Extension:</label>
    <div class="checks">
      <span><i class="box"><svg width="8" height="8" viewBox="0 0 8 8"><path d="M1 4l2 2 4-5" fill="none" stroke="#1b5fae" stroke-width="1.4"/></svg></i>All</span>
      <span><i class="box"><svg width="8" height="8" viewBox="0 0 8 8"><path d="M1 4l2 2 4-5" fill="none" stroke="#1b5fae" stroke-width="1.4"/></svg></i>.com</span>
      <span><i class="box"><svg width="8" height="8" viewBox="0 0 8 8"><path d="M1 4l2 2 4-5" fill="none" stroke="#1b5fae" stroke-width="1.4"/></svg></i>.net</span>
      <span><i class="box"><svg width="8" height="8" viewBox="0 0 8 8"><path d="M1 4l2 2 4-5" fill="none" stroke="#1b5fae" stroke-width="1.4"/></svg></i>.org</span>
    </div>
    <label style="left:16px;top:150px">Price:</label>
    <div class="input" style="left:64px;top:143px;width:46px;height:23px"></div>
    <span class="to" style="left:117px;top:150px">to</span>
    <div class="input" style="left:133px;top:143px;width:47px;height:23px"></div>
    <label style="left:16px;top:181px">Length:</label>
    <div class="input" style="left:64px;top:174px;width:46px;height:23px"></div>
    <span class="to" style="left:117px;top:181px">to</span>
    <div class="input" style="left:133px;top:174px;width:47px;height:23px"></div>
    <div class="find">Find Domains</div>
  </form>
</section>

<section>
  <div class="abs band"></div>
  <h2 class="abs col-title" style="left:107px;top:676px">Safe and Secure</h2>
  <div class="abs feature" style="left:107px;top:716px">
    <svg width="32" height="32" viewBox="0 0 32 32"><circle cx="16" cy="16" r="15" fill="#3d9a1c"/><circle cx="16" cy="16" r="12" fill="none" stroke="#fff" stroke-width="1" stroke-dasharray="2 2"/><path d="M9 16l5 5 9-10" fill="none" stroke="#fff" stroke-width="3.5"/></svg>
    <div><h3>Service you can trust</h3><p>Servicing thousands of clients<br>since 2005.</p></div>
  </div>
  <div class="abs feature" style="left:107px;top:767px">
    <svg width="32" height="32" viewBox="0 0 32 32"><circle cx="16" cy="16" r="15" fill="#3d9a1c"/><path d="M16 6l3 6.5 7 .8-5.2 4.8 1.4 7L16 21.5 9.8 25l1.4-7L6 13.3l7-.8z" fill="#fff"/></svg>
    <div><h3>100% Satisfaction Guaranteed</h3><p>Your satisfaction is our priority!</p></div>
  </div>
  <div class="abs feature" style="left:107px;top:816px">
    <svg width="32" height="32" viewBox="0 0 32 32"><circle cx="16" cy="16" r="15" fill="#3d9a1c"/><circle cx="16" cy="11" r="3.5" fill="#fff"/><path d="M10 24v-5a6 6 0 0 1 12 0v5z" fill="#fff"/></svg>
    <div><h3>Support Center</h3><p>Have a question or comment?</p></div>
  </div>

  <h2 class="abs col-title" style="left:350px;top:676px">The Value of Domains</h2>
  <div class="abs feature" style="left:350px;top:716px">
    <svg width="32" height="32" viewBox="0 0 32 32"><circle cx="16" cy="16" r="15" fill="#0a4f9e"/><rect x="11" y="8" width="10" height="16" rx="5" fill="#fff"/><path d="M16 9v5" stroke="#0a4f9e" stroke-width="1.5"/></svg>
    <div><h3>Domain Valuations</h3><p>Here's what to look for.</p></div>
  </div>
  <div class="abs feature" style="left:350px;top:767px">
    <svg width="32" height="32" viewBox="0 0 32 32"><circle cx="16" cy="16" r="15" fill="#0a4f9e"/><rect x="8" y="12" width="16" height="11" rx="1.5" fill="#fff"/><path d="M13 12v-2h6v2" fill="none" stroke="#fff" stroke-width="1.8"/><path d="M8 16h16" stroke="#0a4f9e"/></svg>
    <div><h3>Business Assets</h3><p>Why domains are critical to business.</p></div>
  </div>
  <div class="abs feature" style="left:350px;top:816px">
    <svg width="32" height="32" viewBox="0 0 32 32"><circle cx="16" cy="16" r="15" fill="#0a4f9e"/><path d="M10.5 10.5l11 11M21.5 10.5l-11 11" stroke="#fff" stroke-width="4"/></svg>
    <div><h3>Avoiding Problems</h3><p>Help buying domain names.</p></div>
  </div>

  <div class="abs promo" role="img" aria-label="Promotional banner: wireframe globe with a computer mouse and a .com tag">
    <p class="get"><span style="font-size:16px">Get your</span><br><span style="font-size:26px">Domain name</span><br><span style="font-size:22px">Today,</span></p>
    <p class="easy">We make<br>it easy!</p>
  </div>
</section>

<section>
  <h2 class="abs testi-title">
    <svg width="34" height="34" viewBox="0 0 34 34"><circle cx="17" cy="17" r="15" fill="#fff" stroke="#333" stroke-width="2.5"/><path d="M9 22v-5c0-3 1.5-5 4.5-6l.5 1.5c-1.5.7-2 1.8-2 3h2.5V22zM18 22v-5c0-3 1.5-5 4.5-6l.5 1.5c-1.5.7-2 1.8-2 3h2.5V22z" fill="#333"/></svg>
    Testimonials
  </h2>
  <blockquote class="abs quotebox">“Lorem ipsum dolor sit amet, consectetur adipisicing elit, sed do eiusmod tempor incididunt ut labore et dolore magna aliqua. Ut enim ad minim veniam, quis nostrud exercitation ullamco laboris nisi ut aliquip ex ea commodo consequat quis nostrud exercitation ullamco laboris nisi ut aliquip ex ea commodo consequat..”</blockquote>
  <svg class="abs quote-tail" width="14" height="9" viewBox="0 0 14 9"><path d="M0 0h14L7 8z" fill="#fff"/><path d="M0 1L7 8 14 1" fill="none" stroke="#ddd"/></svg>
  <p class="abs quote-by">Companyname.com</p>
</section>

<footer class="abs footer">
  <div class="fcol" style="left:409px"><h4>Deleting domains</h4>Traffic score<br>Domain rank<br>Popularity score<br>US based traffic percent</div>
  <div class="fcol" style="left:542px"><h4>Domains for sale</h4>Newest Domains<br>Elite Domains<br>Cheap Domains</div>
  <div class="fcol" style="left:650px"><h4>Support</h4>Terms Of Use</div>
  <div class="fcol" style="left:737px;top:14px"><h4>FAQ</h4>Backorder FAQ<br>Offer FAQ<br>Purchase FAQ</div>
  <div class="frule"></div>
  <div class="social"><i aria-label="Social profile"></i><i aria-label="Social profile"></i></div>
  <p class="copy">Copyright © 2013 zeprilo.com . All rights reserved.</p>
</footer>

</body>
</html>
```